Trade show Banner to be displayed on vertical stand

We are an IT company that specializes in working with Manufacturing companies and manufacturing plants. We need two banners designed for a manufacturing trade show. The design needs to be designed using the supplied template file. Also the design needs to communicate graphically that we specialize in working with manufacturing plants. Also they should communicate that out services include: IT Services, Network, Voice, Data

Target Market(s)

Manufacturing companies

Industry/Entity Type

Manufacturing

Requirements
Must have
• Clear message, clear graphic message. Must be designed with included templates
Nice to have
• Company colors need to be used, but additional colors can be used

```html
<!DOCTYPE html>
<html lang="en">
<head>
<meta charset="utf-8">
<title>Linkforge trade show banners</title>
<link rel="stylesheet" href="https://fonts.googleapis.com/css2?family=Montserrat:wght@300;400;600;800&family=Oswald:wght@600&display=swap">
<style>
  :root {
    --brand-blue: #2872b9;
    --deep-black: #111214;
    --panel-light: #ececec;
    --panel-shade: #dcdcdc;
    --steel-grey: #8a8a8a;
    --white: #ffffff;
    --stage: #2d2d2d;
  }
  html, body {
    margin: 0;
    padding: 0;
    width: 1010px;
    height: 1200px;
    overflow: hidden;
    background: var(--stage);
  }
  .canvas {
    position: relative;
    width: 1010px;
    height: 1200px;
  }
  .banner {
    position: absolute;
    top: 60px;
    width: 426px;
    height: 1078px;
    display: block;
  }
  .banner--plants { left: 54px; }
  .banner--services { left: 526px; }
  .brand-name {
    font-family: "Montserrat", sans-serif;
    font-weight: 600;
    fill: var(--brand-blue);
  }
  .headline-bold {
    font-family: "Oswald", sans-serif;
    font-weight: 600;
    fill: var(--white);
  }
  .headline-light {
    font-family: "Montserrat", sans-serif;
    font-weight: 400;
    fill: var(--white);
  }
  .headline-heavy {
    font-family: "Montserrat", sans-serif;
    font-weight: 800;
    fill: var(--white);
  }
  .service-label {
    font-family: "Montserrat", sans-serif;
    font-weight: 800;
    font-size: 31px;
    fill: var(--white);
  }
  .service-icon {
    fill: none;
    stroke: var(--deep-black);
    stroke-width: 2;
  }
  .service-glyph {
    fill: none;
    stroke: var(--white);
    stroke-width: 1.8;
    stroke-linecap: round;
    stroke-linejoin: round;
  }
  .divider { stroke: var(--white); stroke-width: 1.5; }
  .web-address {
    font-family: "Montserrat", sans-serif;
    font-size: 27px;
    fill: var(--white);
  }
  .web-address .web-strong { font-weight: 800; }
  .web-address .web-plain { font-weight: 400; }
  .fill-blue { fill: var(--brand-blue); }
  .fill-black { fill: var(--deep-black); }
</style>
</head>
<body>
<main class="canvas">

  <!-- Banner one: manufacturing plants message -->
  <svg class="banner banner--plants" viewBox="0 0 426 1078" xmlns="http://www.w3.org/2000/svg">
    <defs>
      <linearGradient id="plants-top" x1="0" y1="0" x2="1" y2="1">
        <stop offset="0" stop-color="#f4f4f4"/>
        <stop offset="1" stop-color="#dedede"/>
      </linearGradient>
      <linearGradient id="plants-photo" x1="0" y1="0" x2="1" y2="1">
        <stop offset="0" stop-color="#9fb4c8"/>
        <stop offset="0.5" stop-color="#3d5670"/>
        <stop offset="1" stop-color="#1c2a3b"/>
      </linearGradient>
      <linearGradient id="plants-grey" x1="0" y1="0" x2="1" y2="0">
        <stop offset="0" stop-color="#5a5a5a"/>
        <stop offset="1" stop-color="#b4b4b4"/>
      </linearGradient>
    </defs>

    <rect class="panel-top" width="426" height="1078" fill="url(#plants-top)"/>

    <g class="brand">
      <circle cx="84" cy="94" r="37" class="fill-blue"/>
      <text class="brand-name" x="140" y="111" font-size="46" textLength="236" lengthAdjust="spacingAndGlyphs">linkforge</text>
    </g>

    <polygon class="accent-band fill-blue" points="0,216 426,144 426,170 0,268"/>
    <g role="img" aria-label="Businessman in a suit drawing a glowing network diagram with cloud, email, device and database icons over a city skyline">
      <polygon points="0,268 426,200 426,640 0,612" fill="url(#plants-photo)"/>
    </g>
    <polygon class="corner-wedge fill-black" points="190,238 426,170 426,200"/>
    <polygon class="grey-wedge" points="0,612 190,676 0,704" fill="url(#plants-grey)"/>
    <polygon class="dark-band fill-black" points="0,704 190,676 426,600 426,640 0,712"/>
    <polygon class="message-panel fill-blue" points="0,712 426,636 426,1004 0,1004"/>

    <g class="headline">
      <text class="headline-bold" x="49" y="800" font-size="46" textLength="330" lengthAdjust="spacingAndGlyphs">WE SPECIALIZE IN</text>
      <text class="headline-light" x="78" y="848" font-size="34" textLength="272" lengthAdjust="spacingAndGlyphs">WORKING WITH</text>
      <text class="headline-bold" x="49" y="900" font-size="46" textLength="330" lengthAdjust="spacingAndGlyphs">MANUFACTURING</text>
      <text class="headline-heavy" x="47" y="986" font-size="82" textLength="334" lengthAdjust="spacingAndGlyphs">PLANTS</text>
    </g>

    <rect class="footer fill-black" x="0" y="1004" width="426" height="74"/>
    <text class="web-address" x="213" y="1050" text-anchor="middle"><tspan class="web-plain">www.</tspan><tspan class="web-strong">lkfit</tspan><tspan class="web-plain">.com</tspan></text>
  </svg>

  <!-- Banner two: services list -->
  <svg class="banner banner--services" viewBox="0 0 426 1078" xmlns="http://www.w3.org/2000/svg">
    <defs>
      <linearGradient id="services-top" x1="0" y1="0" x2="1" y2="1">
        <stop offset="0" stop-color="#f4f4f4"/>
        <stop offset="1" stop-color="#dedede"/>
      </linearGradient>
      <linearGradient id="services-photo" x1="0" y1="0" x2="1" y2="0">
        <stop offset="0" stop-color="#d9dde0"/>
        <stop offset="0.55" stop-color="#9aa3a8"/>
        <stop offset="1" stop-color="#2a2c30"/>
      </linearGradient>
      <linearGradient id="services-grey" x1="0" y1="0" x2="1" y2="0">
        <stop offset="0" stop-color="#5a5a5a"/>
        <stop offset="1" stop-color="#b4b4b4"/>
      </linearGradient>
    </defs>

    <rect class="panel-top" width="426" height="1078" fill="url(#services-top)"/>

    <g class="brand">
      <circle cx="84" cy="94" r="37" class="fill-blue"/>
      <text class="brand-name" x="140" y="111" font-size="46" textLength="236" lengthAdjust="spacingAndGlyphs">linkforge</text>
    </g>

    <polygon class="accent-band fill-blue" points="0,216 426,144 426,170 0,268"/>
    <g role="img" aria-label="IT technician in a suit working on a laptop in front of server racks in a data centre">
      <polygon points="0,268 426,200 426,640 0,612" fill="url(#services-photo)"/>
    </g>
    <polygon class="corner-wedge fill-black" points="190,238 426,170 426,200"/>
    <polygon class="grey-wedge" points="0,612 190,676 0,704" fill="url(#services-grey)"/>
    <polygon class="dark-band fill-black" points="0,704 190,676 426,600 426,640 0,712"/>
    <polygon class="message-panel fill-blue" points="0,712 426,636 426,1004 0,1004"/>

    <g class="service-list">
      <!-- IT services -->
      <circle class="service-icon" cx="88" cy="754" r="26"/>
      <g class="service-glyph">
        <circle cx="86" cy="756" r="11"/>
        <ellipse cx="86" cy="756" rx="5" ry="11"/>
        <line x1="75" y1="756" x2="97" y2="756"/>
        <path d="M97 748 L102 744 L102 738"/>
      </g>
      <line class="divider" x1="140" y1="730" x2="140" y2="778"/>
      <text class="service-label" x="168" y="766">IT SERVICES</text>

      <!-- Network -->
      <circle class="service-icon" cx="88" cy="821" r="26"/>
      <g class="service-glyph">
        <circle cx="88" cy="821" r="4"/>
        <circle cx="78" cy="810" r="3"/>
        <circle cx="99" cy="810" r="3"/>
        <circle cx="78" cy="833" r="3"/>
        <circle cx="99" cy="833" r="3"/>
        <path d="M85 818 L80 812 M91 818 L97 812 M85 824 L80 831 M91 824 L97 831"/>
      </g>
      <line class="divider" x1="140" y1="797" x2="140" y2="845"/>
      <text class="service-label" x="168" y="833">NETWORK</text>

      <!-- Voice -->
      <circle class="service-icon" cx="88" cy="889" r="26"/>
      <g class="service-glyph">
        <rect x="83" y="874" width="10" height="18" rx="5"/>
        <path d="M78 887 a10 10 0 0 0 20 0"/>
        <line x1="88" y1="897" x2="88" y2="904"/>
        <line x1="82" y1="904" x2="94" y2="904"/>
      </g>
      <line class="divider" x1="140" y1="865" x2="140" y2="913"/>
      <text class="service-label" x="168" y="901">VOICE</text>

      <!-- Data -->
      <circle class="service-icon" cx="88" cy="956" r="26"/>
      <g class="service-glyph">
        <rect x="76" y="950" width="14" height="5" rx="1"/>
        <rect x="76" y="957" width="14" height="5" rx="1"/>
        <rect x="76" y="964" width="14" height="5" rx="1"/>
        <circle cx="98" cy="946" r="4"/>
        <path d="M97 956 L97 968 M94 960 L97 956 L100 960"/>
      </g>
      <line class="divider" x1="140" y1="932" x2="140" y2="980"/>
      <text class="service-label" x="168" y="968">DATA</text>
    </g>

    <rect class="footer fill-black" x="0" y="1004" width="426" height="74"/>
    <text class="web-address" x="213" y="1050" text-anchor="middle"><tspan class="web-plain">www.</tspan><tspan class="web-strong">lkfit</tspan><tspan class="web-plain">.com</tspan></text>
  </svg>

</main>
</body>
</html>
```